Handout for attendees of educational seminar

I provide educational workshops on how to give technical presentations at conferences to scientists and engineers. My company is called Craft Talk Studio (www.CraftTalkStudio.example). I would like a double sided, half page size flyer that can be used as a handout for attendees of my workshops. On one side of the flyer, they will get top tips for creating their next presentation. On the other side, they will get my photo, bio, and contact information. I have uploaded a draft of a full page design I made myself. I'd like the copy of the tips to remain the same, but everything else is flexible.

Target Market(s)

scientists, engineers, technical professionals

Font styles to use
Serif
Sans Serif

Requirements
Must have
• my photo (I've provided two options to choose from depending on colors...photo on side 2 only), my logo, flyer needs to be half page in size (5.5" x 8.5"), needs to be double sided, One side has the "tips" and the other side has my personal details (see attached page for copy).
Nice to have
• I like the use of icons on the "tips" side of the flyer.

```html
<!DOCTYPE html>
<html lang="en">
<head>
<meta charset="utf-8">
<title>Craft Talk Studio – Workshop Handout</title>
<link rel="stylesheet" href="https://fonts.googleapis.com/css2?family=Lato:ital,wght@0,300;0,400;0,700;1,700;1,900&family=Roboto:wght@500;700&family=Rubik:wght@500;600&family=Ubuntu:wght@500&display=swap">
<style>
  :root{
    --teal:#1c6a85;
    --teal-dark:#0f4a5e;
    --green:#7ab648;
    --green-dark:#5a8f2f;
    --ink:#333;
    --mark:#4b4b4b;
    --paper:#f7f7f7;
    --card:#ffffff;
    --stage:#c4c4c4;
  }
  *{box-sizing:border-box;margin:0;padding:0}
  html,body{width:1200px;height:1200px;overflow:hidden}
  body{background:var(--stage);font-family:"Lato",sans-serif;color:var(--ink);position:relative}
  .page{position:absolute;top:240px;width:473px;height:720px;background:var(--paper);overflow:hidden}
  .page--tips{left:90px}
  .page--bio{left:638px}

  .brand{position:absolute;text-align:center;width:160px}
  .brand__dot{width:52px;height:52px;border-radius:50%;background:var(--mark);margin:0 auto 6px}
  .brand__name{font-family:"Lato",sans-serif;font-weight:300;font-size:18px;color:var(--green);white-space:nowrap}

  .tips-header{position:absolute;left:0;top:0;width:100%;height:105px;background:#fff}
  .tips-header .brand{left:157px;top:20px}
  .hero{position:absolute;left:0;top:105px;width:100%;height:139px;background:linear-gradient(90deg,#1a6581,#237590 50%,#1a6581);color:#fff;text-align:center}
  .hero__kicker{font-family:"Roboto",sans-serif;font-weight:500;font-size:26px;margin-top:10px}
  .hero__title{font-family:"Roboto",sans-serif;font-weight:700;font-size:62px;line-height:58px;letter-spacing:1px}
  .hero__rule{width:340px;height:2px;background:#fff;margin:2px auto 0}
  .hero__sub{font-family:"Lato",sans-serif;font-size:16px;font-weight:400;margin-top:6px}

  .tip{position:absolute;left:0;width:100%}
  .tip__card{position:absolute;background:var(--card);border-radius:30px;box-shadow:0 3px 6px rgba(0,0,0,.18)}
  .tip__tab{position:absolute;height:27px;color:#fff;font-family:"Rubik",sans-serif;font-weight:600;font-size:18px;line-height:27px;text-align:center;letter-spacing:.3px}
  .tip__tab--green{background:var(--green);clip-path:polygon(4% 0,100% 0,97% 100%,0 100%)}
  .tip__tab--teal{background:var(--teal);clip-path:polygon(3% 0,100% 0,96% 100%,0 100%)}
  .tip__icon{position:absolute;width:78px;height:78px;border-radius:50%;background:#fff;display:flex;align-items:center;justify-content:center;box-shadow:0 2px 5px rgba(0,0,0,.2)}
  .tip__icon--green{border:6px solid var(--green)}
  .tip__icon--teal{border:6px solid var(--teal)}
  .tip__text{position:absolute;font-size:9.6px;line-height:12px;color:#333;text-align:justify}
  .tip__text p+p{margin-top:6px}
  .tip__label{font-weight:700;font-size:11.5px}
  .tip__label--green{color:var(--green-dark)}
  .tip__label--teal{color:var(--teal)}

  .cta{position:absolute;left:24px;top:632px;width:430px;font-style:italic;font-weight:700;font-size:13.2px;line-height:17px;color:#222}

  .footer{position:absolute;left:0;bottom:0;width:100%;height:47px;background:var(--teal);color:#fff;font-size:12px;display:flex;align-items:center;justify-content:space-between;padding:0 26px}
  .footer__item{display:flex;align-items:center;gap:7px}

  .bio-header{position:absolute;left:0;top:0;width:100%;height:113px;background:#fff}
  .bio-header .brand{left:10px;top:26px}
  .bio-header__line{position:absolute;left:176px;top:40px;font-family:"Ubuntu",sans-serif;font-weight:500;font-size:22px;line-height:25px;color:var(--teal);white-space:nowrap}
  .photo{position:absolute;left:0;top:113px;width:100%;height:283px;background:radial-gradient(ellipse at 62% 55%,#d8243c 0%,#a8142c 35%,#5a0b1c 70%,#1b0710 100%)}
  .bio{position:absolute;left:24px;top:410px;width:424px}
  .bio__title{font-family:"Rubik",sans-serif;font-weight:600;font-size:18px;color:var(--green);margin-bottom:6px}
  .bio p{font-size:9.5px;line-height:12px;text-align:justify;margin-bottom:12px;color:#333}
</style>
</head>
<body>

<section class="page page--tips">
  <header class="tips-header">
    <div class="brand"><div class="brand__dot"></div><div class="brand__name">Dana Whitfield</div></div>
  </header>

  <div class="hero">
    <div class="hero__kicker">Craft Talk Studio</div>
    <div class="hero__title">QUICK TIPS</div>
    <div class="hero__rule"></div>
    <div class="hero__sub">Science not communicated is science not done!</div>
  </div>

  <article class="tip" style="top:258px">
    <div class="tip__card" style="left:30px;top:12px;width:414px;height:96px"></div>
    <div class="tip__tab tip__tab--green" style="left:124px;top:0;width:320px">Be Audience Centered</div>
    <div class="tip__icon tip__icon--green" style="left:31px;top:23px">
      <svg width="34" height="34" viewBox="0 0 34 34" fill="none" stroke="#5cb85c" stroke-width="3.2" stroke-linecap="round" stroke-linejoin="round"><path d="M7 18l7 7 13-15"/></svg>
    </div>
    <div class="tip__text" style="left:148px;top:36px;width:285px">
      <p>Your ability to be successful as a speaker depends upon your ability to make your audience successful.</p>
      <p><span class="tip__label tip__label--green">TIP:</span> Return to "Points of Common Ground" throughout the talk that answer the question "So what?" about the scientific info. Be an interpreter!</p>
    </div>
  </article>

  <article class="tip" style="top:384px">
    <div class="tip__card" style="left:28px;top:12px;width:412px;height:94px"></div>
    <div class="tip__tab tip__tab--teal" style="left:26px;top:0;width:320px">Filter &amp; Focus</div>
    <div class="tip__icon tip__icon--teal" style="left:362px;top:24px">
      <svg width="34" height="34" viewBox="0 0 34 34" fill="none" stroke="#2b8fd6" stroke-width="2.6" stroke-linejoin="round"><path d="M5 7h24l-9 11v9l-6-3v-6z"/></svg>
    </div>
    <div class="tip__text" style="left:54px;top:43px;width:290px">
      <p>When you try to share everything, you share nothing.</p>
      <p><span class="tip__label tip__label--teal">TIP:</span> Start your planning with the "view" you want your audience to have at the end of the talk. Then ask yourself "What would they need to know in order to get there?"</p>
    </div>
  </article>

  <article class="tip" style="top:509px">
    <div class="tip__card" style="left:30px;top:12px;width:414px;height:96px"></div>
    <div class="tip__tab tip__tab--green" style="left:124px;top:0;width:320px">Show Your Science</div>
    <div class="tip__icon tip__icon--green" style="left:31px;top:23px">
      <svg width="34" height="34" viewBox="0 0 34 34"><path d="M5 29h24" stroke="#3b3b3b" stroke-width="2.4" stroke-linecap="round"/><rect x="8" y="17" width="5" height="10" fill="#5cb85c"/><rect x="15" y="10" width="5" height="17" fill="#3b3b3b"/><rect x="22" y="5" width="5" height="22" fill="#5cb85c"/></svg>
    </div>
    <div class="tip__text" style="left:148px;top:36px;width:285px">
      <p>Your slides should do something for you that your words cannot. This means make your slides VISUAL not VERBAL.</p>
      <p><span class="tip__label tip__label--green">TIP:</span> Have a brief take-away messages supported by visual evidence.</p>
    </div>
  </article>

  <p class="cta">Need more help? Check out Dana Whitfield's Craft Talk Studio Boot Camp training program. Includes 1:1 Coaching!</p>

  <footer class="footer">
    <span class="footer__item"><svg width="15" height="15" viewBox="0 0 16 16"><circle cx="8" cy="8" r="8" fill="#fff"/><rect x="4" y="5" width="8" height="6" fill="none" stroke="#1c6a85" stroke-width="1.3"/><path d="M4 5l4 3 4-3" fill="none" stroke="#1c6a85" stroke-width="1.3"/></svg>hello@crafttalkstudio.example</span>
    <span class="footer__item"><svg width="15" height="15" viewBox="0 0 16 16" fill="none" stroke="#fff" stroke-width="1.2"><circle cx="8" cy="8" r="7"/><ellipse cx="8" cy="8" rx="3" ry="7"/><path d="M1 8h14M2.5 4.5h11M2.5 11.5h11"/></svg>www.CraftTalkStudio.example</span>
  </footer>
</section>

<section class="page page--bio">
  <header class="bio-header">
    <div class="brand"><div class="brand__dot"></div><div class="brand__name">Dana Whitfield</div></div>
    <div class="bio-header__line">Science not communicated<br>is science not done!</div>
  </header>

  <div class="photo" role="img" aria-label="Photo of the speaker presenting on a red-lit lecture stage"></div>

  <div class="bio">
    <h2 class="bio__title">Meet Dana</h2>
    <p>Dana Whitfield is on a mission: to transform how scientists, engineers, and technical professionals present their work. That's because she believes that even the best technical ideas are destined to remain undiscovered unless presented in a clear and compelling way that sparks innovation and drives adoption.</p>
    <p>For a decade, she's traveled around the world to work with Global 100 corporations, institutions and universities, teaching the proven strategies she's mastered through her consulting work and during her time as a faculty member Northfield State University.</p>
    <p>Dana is internationally known for her popular talk entitled "Talk Technical to Me" which has over 2 million views (and counting!).</p>
    <p>Teams that work with Dana get the practical skills and natural confidence they need to immediately shift their "information dump"-style presentations into ones that are meaningful, engaging, and inspire people to take action.</p>
    <p>Dana provides on-site group workshops and coaching, conference sessions and keynotes, and 1:1 consultation.</p>
  </div>

  <footer class="footer">
    <span class="footer__item"><svg width="15" height="15" viewBox="0 0 16 16"><circle cx="8" cy="8" r="8" fill="#fff"/><rect x="4" y="5" width="8" height="6" fill="none" stroke="#1c6a85" stroke-width="1.3"/><path d="M4 5l4 3 4-3" fill="none" stroke="#1c6a85" stroke-width="1.3"/></svg>hello@crafttalkstudio.example</span>
    <span class="footer__item"><svg width="15" height="15" viewBox="0 0 16 16" fill="none" stroke="#fff" stroke-width="1.2"><circle cx="8" cy="8" r="7"/><ellipse cx="8" cy="8" rx="3" ry="7"/><path d="M1 8h14M2.5 4.5h11M2.5 11.5h11"/></svg>www.CraftTalkStudio.example</span>
  </footer>
</section>

</body>
</html>
```